Require an amazing and engaging Home Page redesign! For New Startup!

We require a new design for our home page of www.quorvex.com.au.

We want this to be in a similar theme to the current site, all other pages to remain unchanged however our marketing team have advised that the current home page (initial banner) is not engaging or "hooking" potential leads. I have attached "CRO Recommendations" from our marketing team as an idea to the issues with the Quorvex site.
At the moment we would only like the issues on home page reviewed (Pages: 4 to 10).

I have attached an example from our marketing team as to an idea of how the front home page needs to look.

As an idea of what our competition is doing well please view zentrimo.com.au, plavotrek.com.au (great engagement on home page top banner).

Quorvex is a brand new concept for Australian new car buyers. Quorvex allows a customer buying a new car to receive best price offer for their new car needs and finance requirements all on a sophisticated online dashboard. The dashboard even allows the customer to interact directly with the dealerships to negotiate the price online! (never offered before).

I've provided new logo, brand guidelines for colour and font scheme.

View the website to get an idea of what Quorvex is all about and let's see what we can come up with.

Thanks.

Target Market(s)

Females, age between 21-35

Industry/Entity Type

Automotive

Number of Pages Required

1 page

Requirements
Must have
• Engaging initial banner. We want to see the banner as mocked up and provided but also maybe provide an option showing a large graphic as the banner that incorporates this "hook" for engagement.
• Minimal menu (no Need Help or Newsletter buttons) with new logo on left.
• As per design mockup. Looking for engaging banner.
• Why it Works benefits section - 3 to 4 key benefits
• Customer satisfaction/testimonial area
Nice to have
• As Seen On banner or icon somewhere - maybe near or under the "Get Offers' buttons? As we have been featured in the MERIDIAN POST

```html
<!DOCTYPE html>
<html lang="en">
<head>
<meta charset="utf-8">
<title>Quorvex – A Revolution in Car Buying</title>
<link href="https://fonts.googleapis.com/css2?family=Nunito+Sans:wght@300;400;600;700&display=swap" rel="stylesheet">
<style>
:root{
  --brand-blue:#2a78ad;
  --brand-navy:#1d4f73;
  --band-blue:#2f78a8;
  --button-blue:#2b6a98;
  --gold:#e9a91d;
  --ink:#222;
  --muted:#888;
  --light-text:#9a9a9a;
  --grey-band:#efefef;
  --line:#d9d9d9;
  --white:#fff;
}
*{box-sizing:border-box;margin:0;padding:0}
html,body{width:1200px;height:2927px;overflow:hidden}
body{font-family:"Nunito Sans",Arial,sans-serif;color:var(--ink);background:var(--white);position:relative}
h1,h2,h3,h4,h5{font-weight:400}
.abs{position:absolute}

/* Header */
.site-header{position:absolute;left:0;top:0;width:1200px;height:98px;background:var(--white);border-bottom:1px solid #e6e6e6}
.brand-name{position:absolute;left:198px;top:28px;font-size:36px;font-weight:700;color:var(--brand-blue);letter-spacing:.5px;line-height:44px}
.main-nav{position:absolute;left:444px;top:38px;display:flex;gap:40px;font-size:18px;color:#777}
.phone{position:absolute;left:945px;top:36px;display:flex;align-items:center;gap:12px;font-size:19px;font-weight:700;color:var(--ink)}
.phone-icon{width:22px;height:22px;background:var(--gold);border-radius:4px;display:flex;align-items:center;justify-content:center}

/* Hero */
.hero{position:absolute;left:0;top:98px;width:1200px;height:556px;background:radial-gradient(ellipse at 50% 40%,#f7f7f7 0%,#e6e6e6 70%,#dcdcdc 100%)}
.hero-title{position:absolute;top:44px;width:100%;text-align:center;font-size:35px;font-weight:700;color:var(--brand-navy)}
.hero-sub{position:absolute;top:90px;width:100%;text-align:center;font-size:25px;color:var(--brand-blue)}
.hero-card{position:absolute;left:137px;top:169px;width:936px;height:309px;background:var(--white);border-radius:18px;box-shadow:0 2px 8px rgba(0,0,0,.15)}
.hero-photo{position:absolute;left:31px;top:-31px;width:245px;height:340px;background:linear-gradient(180deg,#d8cfc4 0%,#b59a82 40%,#46c1ec 70%,#3ab7e6 100%);border-radius:6px 6px 0 18px}
.step{position:absolute;top:44px;width:190px;text-align:center;font-size:16px;line-height:23px;color:#444}
.step-circle{width:120px;height:120px;border-radius:50%;margin:0 auto 14px;position:relative;display:flex;align-items:center;justify-content:center}
.step-num{position:absolute;left:-4px;top:-4px;width:38px;height:38px;border-radius:50%;border:2px solid var(--white);color:var(--white);font-size:22px;display:flex;align-items:center;justify-content:center}
.step-1 .step-circle{background:radial-gradient(circle at 40% 35%,#f3c23c,#d99412)}
.step-1 .step-num{background:#e9a91d}
.step-2 .step-circle{background:radial-gradient(circle at 40% 35%,#3d8fc5,#1f6397)}
.step-2 .step-num{background:#2c7ab2}
.step-3 .step-circle{background:radial-gradient(circle at 40% 35%,#2f75a6,#17486f)}
.step-3 .step-num{background:#215a86}
.slider-dots{position:absolute;top:512px;left:544px;display:flex;gap:10px}
.slider-dots span{width:14px;height:14px;border-radius:50%;background:#555}
.slider-dots span.active{background:transparent;border:2px solid #555}

/* Choose */
.choose{position:absolute;left:0;top:654px;width:1200px;height:595px;background:var(--white);border-top:1px solid #e3e3e3}
.section-title{position:absolute;width:100%;text-align:center;font-size:29px;font-weight:600;color:var(--ink)}
.offer-card{position:absolute;top:134px;width:318px;height:418px;background:var(--white);border:1px solid #e2e2e2;box-shadow:0 1px 5px rgba(0,0,0,.12)}
.offer-photo{height:94px;width:100%}
.offer-title{margin:38px 24px 0;text-align:center;font-size:14.5px;line-height:19px;color:#333;text-transform:uppercase}
.checks{list-style:none;margin:18px 0 0 44px;font-size:11px;color:#333}
.checks li{display:flex;align-items:center;gap:10px;height:25px}
.tick{width:10px;height:8px}
.select{position:absolute;left:26px;width:265px;height:28px;border:1px solid #ccc;border-radius:2px;font-size:11px;color:#555;padding:6px 10px}
.select::after{content:"";position:absolute;right:0;top:0;width:22px;height:26px;border-left:1px solid #ccc}
.select i{position:absolute;right:7px;top:11px;border-left:4px solid transparent;border-right:4px solid transparent;border-top:5px solid #444;z-index:1}
.loan-input{position:absolute;left:26px;top:304px;width:265px;height:38px;border:1px solid #ccc;border-radius:3px;font-size:11px;color:#555;padding:11px 12px}
.btn-offers{position:absolute;left:100px;top:368px;width:117px;height:30px;background:var(--button-blue);color:var(--white);font-size:12px;text-align:center;line-height:30px;border-radius:2px}
.ribbon{position:absolute;left:74px;top:-18px;width:170px;height:34px;background:var(--gold);color:var(--white);font-size:16px;text-align:center;line-height:34px;border-radius:2px;z-index:2}

/* Testimonials */
.testimonials{position:absolute;left:0;top:1249px;width:1200px;height:467px;background:var(--grey-band);border-top:1px solid #dcdcdc}
.testimonials .section-title{top:58px;color:var(--brand-blue);font-weight:400;font-size:27px}
.review{position:absolute;top:140px;width:200px}
.stars{display:flex;gap:2px;margin-bottom:10px}
.review h3{font-size:15.5px;font-weight:600;color:#333;margin-bottom:10px}
.review p{font-size:14.5px;line-height:22.5px;color:var(--light-text)}
.review .author{margin-top:12px;font-size:14px;color:var(--brand-blue)}
.arrow{position:absolute;top:196px}
.rating{position:absolute;top:373px;width:100%;text-align:center;font-size:15px;color:#aaa}

/* Why it works */
.why{position:absolute;left:0;top:1716px;width:1200px;height:502px;background:linear-gradient(180deg,#3079a9 0%,#2b72a2 100%)}
.why-tab{position:absolute;left:390px;top:-44px;width:425px;height:46px}
.why-title{position:absolute;left:390px;top:-22px;width:425px;text-align:center;font-size:29px;line-height:40px;color:var(--white)}
.why-sub{position:absolute;left:254px;top:110px;font-size:26px;color:var(--white)}
.benefit{position:absolute;top:180px;width:160px;text-align:center;color:var(--white)}
.benefit h4{font-size:16px;margin-top:30px}
.benefit p{font-size:11px;line-height:18px;margin-top:6px}
.btn-outline{position:absolute;left:294px;top:397px;width:130px;height:36px;border:1px solid var(--white);border-radius:18px;color:var(--white);text-align:center;line-height:34px;font-size:13px}
.video{position:absolute;left:624px;top:105px;width:488px;height:303px;border:3px solid var(--white);background:linear-gradient(135deg,#8a9aa6 0%,#5c6d7a 45%,#2f3a44 100%)}
.play{position:absolute;left:216px;top:123px}

/* Deals */
.deals{position:absolute;left:0;top:2218px;width:1200px;height:504px;background:var(--white)}
.deals-title{position:absolute;top:50px;width:100%;text-align:center;font-size:27px;line-height:39px;color:var(--ink)}
.deal{position:absolute;top:170px;width:240px;text-align:center}
.deal-car{position:absolute;left:0;top:40px;width:240px;height:128px;border-radius:48% 52% 18% 18%/60% 60% 20% 20%}
.price{position:absolute;left:6px;top:0;width:78px;height:78px;border-radius:50%;background:var(--gold);color:var(--white);z-index:2;padding-top:14px}
.price b{display:block;font-size:24px;line-height:26px;font-weight:600}
.price span{display:block;font-size:12px}
.deal h5{position:absolute;top:188px;width:100%;font-size:18px;color:var(--brand-blue)}
.deal p{position:absolute;top:220px;width:100%;font-size:12.5px;line-height:22px;color:var(--light-text)}

/* Footer */
.site-footer{position:absolute;left:0;top:2722px;width:1200px;height:205px;background:var(--brand-navy);color:var(--white);text-align:center}
.footer-links{position:absolute;top:46px;width:100%;font-size:16px}
.footer-links span{margin:0 8px}
.legal{position:absolute;top:82px;width:100%;font-size:14px;color:#d7e3ec}
.social{position:absolute;left:436px;top:138px;display:flex;gap:12px}
.social span{width:28px;height:28px;border-radius:50%;background:var(--white)}
.footer-brand{position:absolute;left:626px;top:132px;font-size:28px;font-weight:700;color:var(--white);line-height:38px}
</style>
</head>
<body>
<svg width="0" height="0" style="position:absolute">
  <defs>
    <symbol id="star" viewBox="0 0 20 20"><path d="M10 1.5l2.5 5.4 5.9.6-4.4 4 1.2 5.8L10 14.4l-5.2 2.9L6 11.5l-4.4-4 5.9-.6z" fill="none" stroke="#e9a91d" stroke-width="1.5"/></symbol>
    <symbol id="check" viewBox="0 0 10 8"><path d="M1 4l3 3 5-6" fill="none" stroke="#2b6a98" stroke-width="2"/></symbol>
    <symbol id="car" viewBox="0 0 60 34"><path d="M6 24v-7l6-9h36l6 9v7z" fill="#fff"/><circle cx="16" cy="26" r="5" fill="#fff" stroke="#2f78a8" stroke-width="2"/><circle cx="44" cy="26" r="5" fill="#fff" stroke="#2f78a8" stroke-width="2"/><rect x="15" y="11" width="30" height="6" fill="#2f78a8"/></symbol>
  </defs>
</svg>

<header class="site-header">
  <div class="brand-name">Quorvex</div>
  <nav class="main-nav"><span>How it works</span><span>Pricing</span><span>FAQ</span><span>Apply</span><span>Login</span></nav>
  <div class="phone">
    <span class="phone-icon"><svg width="14" height="14" viewBox="0 0 24 24"><path d="M6.6 10.8a15 15 0 006.6 6.6l2.2-2.2a1 1 0 011-.2 11 11 0 003.6.6 1 1 0 011 1V20a1 1 0 01-1 1A17 17 0 013 4a1 1 0 011-1h3.5a1 1 0 011 1 11 11 0 00.6 3.6 1 1 0 01-.3 1z" fill="#fff"/></svg></span>
    1300 555 018
  </div>
</header>

<section class="hero">
  <h1 class="hero-title">A Revolution in Car Buying Has Arrived</h1>
  <p class="hero-sub">Get car dealers and lenders to bid for YOUR business today</p>
  <div class="hero-card">
    <div class="hero-photo" role="img" aria-label="Smiling woman holding a large blue cardboard car cut-out"></div>
    <div class="step step-1" style="left:280px">
      <div class="step-circle"><span class="step-num">1</span>
        <svg width="48" height="48" viewBox="0 0 48 48"><rect x="6" y="22" width="9" height="20" fill="none" stroke="#fff" stroke-width="2.5"/><path d="M15 24l8-14c3 0 4 2 3 6l-1 5h12c2 0 3 2 2 4l-4 14c-1 2-2 3-4 3H15" fill="none" stroke="#fff" stroke-width="2.5"/></svg>
      </div>
      Submit You Car or<br>Finance Needs
    </div>
    <div class="step step-2" style="left:482px">
      <div class="step-circle"><span class="step-num">2</span>
        <svg width="50" height="50" viewBox="0 0 50 50"><circle cx="25" cy="15" r="9" fill="none" stroke="#fff" stroke-width="2.5"/><path d="M8 46c0-11 7-18 17-18s17 7 17 18" fill="none" stroke="#fff" stroke-width="2.5"/><path d="M25 29l-3 5 3 10 3-10z" fill="#fff"/></svg>
      </div>
      Dealerships<br>and lenders submit<br>their best offers
    </div>
    <div class="step step-3" style="left:670px">
      <div class="step-circle"><span class="step-num">3</span>
        <svg width="46" height="52" viewBox="0 0 46 52"><path d="M17 28V8a4 4 0 018 0v14l12 3c3 1 4 3 4 6l-2 13c-1 4-3 6-7 6H22c-3 0-5-1-7-4l-8-10c-2-3 1-6 4-4l6 5" fill="none" stroke="#fff" stroke-width="2.5"/></svg>
      </div>
      You choose the best<br>deal online and<br>exchange contact<br>details. It's that easy!
    </div>
    <svg class="abs" style="left:400px;top:76px" width="70" height="24" viewBox="0 0 70 24"><path d="M2 20Q35 -4 64 14" fill="none" stroke="#bbb" stroke-width="1.5"/><path d="M58 8l7 7-9 2" fill="none" stroke="#bbb" stroke-width="1.5"/></svg>
    <svg class="abs" style="left:600px;top:76px" width="70" height="24" viewBox="0 0 70 24"><path d="M2 20Q35 -4 64 14" fill="none" stroke="#bbb" stroke-width="1.5"/><path d="M58 8l7 7-9 2" fill="none" stroke="#bbb" stroke-width="1.5"/></svg>
  </div>
  <div class="slider-dots"><span class="active"></span><span></span><span></span><span></span></div>
</section>

<section class="choose">
  <h2 class="section-title" style="top:50px">Choose your Car to Get Started</h2>

  <article class="offer-card" style="left:80px">
    <div class="offer-photo" role="img" aria-label="Woman with raised arms in a convertible" style="background:linear-gradient(180deg,#7c8f8a,#3e4a47)"></div>
    <h3 class="offer-title">I just need the best deals<br>on a new car.</h3>
    <ul class="checks"><li><svg class="tick"><use href="#check"/></svg>3 Dealership BEST PRICE car quotes</li></ul>
    <div class="select" style="top:279px">car Model<i></i></div>
    <div class="select" style="top:320px">car Make<i></i></div>
    <div class="btn-offers">GET OFFERS</div>
  </article>

  <article class="offer-card" style="left:435px">
    <span class="ribbon">Most Popular</span>
    <div class="offer-photo" role="img" aria-label="Woman signing car finance paperwork" style="background:linear-gradient(180deg,#8c8c8c,#3a3a3a)"></div>
    <h3 class="offer-title">I need the best deals on a new<br>car and finance.</h3>
    <ul class="checks"><li><svg class="tick"><use href="#check"/></svg>3 Dealership BEST PRICE car quotes</li><li><svg class="tick"><use href="#check"/></svg>3 car finance quotes from our broker panel</li></ul>
    <div class="select" style="top:279px">car Model<i></i></div>
    <div class="select" style="top:320px">car Make<i></i></div>
    <div class="btn-offers">GET OFFERS</div>
  </article>

  <article class="offer-card" style="left:790px">
    <div class="offer-photo" role="img" aria-label="Yellow sports car on the road" style="background:linear-gradient(180deg,#6f6a5a,#c9a23c 60%,#3b3a33)"></div>
    <h3 class="offer-title">I just want the best deal on<br>my car finance,</h3>
    <ul class="checks" style="font-size:10.5px"><li style="height:24px"><svg class="tick"><use href="#check"/></svg>Perfect for NEW OR USED cars</li><li style="height:24px"><svg class="tick"><use href="#check"/></svg>Receive up to 3 live loan quotes</li><li style="height:24px"><svg class="tick"><use href="#check"/></svg>Guaranteed to beat Dealership finance</li><li style="height:24px"><svg class="tick"><use href="#check"/></svg>Quotes from our award-winning broker panel</li></ul>
    <div class="loan-input">$ &nbsp;Estimated Loan Amount</div>
    <div class="btn-offers">GET OFFERS</div>
  </article>
</section>

<section class="testimonials">
  <h2 class="section-title">See What Our Customer Says</h2>
  <svg class="arrow" style="left:46px" width="20" height="36" viewBox="0 0 20 36"><path d="M18 2L3 18l15 16" fill="none" stroke="#bbb" stroke-width="3"/></svg>
  <svg class="arrow" style="left:1128px" width="20" height="36" viewBox="0 0 20 36"><path d="M2 2l15 16L2 34" fill="none" stroke="#bbb" stroke-width="3"/></svg>
  <div class="review" style="left:111px"><div class="stars"><svg width="18" height="18"><use href="#star"/></svg><svg width="18" height="18"><use href="#star"/></svg><svg width="18" height="18"><use href="#star"/></svg><svg width="18" height="18"><use href="#star"/></svg></div><h3>Excellent- No Reservation</h3><p>Arcu Morbi porta libero id ullamcorper nonummy nibh ligula pulvinar metus eget consectetuer augue</p><p class="author">- LENA MARSH</p></div>
  <div class="review" style="left:371px"><div class="stars"><svg width="18" height="18"><use href="#star"/></svg><svg width="18" height="18"><use href="#star"/></svg><svg width="18" height="18"><use href="#star"/></svg><svg width="18" height="18"><use href="#star"/></svg></div><h3>Awesome!</h3><p>Arcu Morbi porta libero id ullamcorper nonummy nibh ligula pulvinar metus eget consectetuer augue</p><p class="author">- LENA MARSH</p></div>
  <div class="review" style="left:638px"><div class="stars"><svg width="18" height="18"><use href="#star"/></svg><svg width="18" height="18"><use href="#star"/></svg><svg width="18" height="18"><use href="#star"/></svg><svg width="18" height="18"><use href="#star"/></svg></div><h3>Professional</h3><p>Arcu Morbi porta libero id ullamcorper nonummy nibh ligula pulvinar metus eget consectetuer augue</p><p class="author">- LENA MARSH</p></div>
  <div class="review" style="left:897px"><div class="stars"><svg width="18" height="18"><use href="#star"/></svg><svg width="18" height="18"><use href="#star"/></svg><svg width="18" height="18"><use href="#star"/></svg><svg width="18" height="18"><use href="#star"/></svg></div><h3>Best Customer Service</h3><p>Arcu Morbi porta libero id ullamcorper nonummy nibh ligula pulvinar metus eget consectetuer augue</p><p class="author">- LENA MARSH</p></div>
  <p class="rating">Rated 9.3 out of &nbsp;10 based on 302 Reviews</p>
</section>

<section class="why">
  <svg class="why-tab" viewBox="0 0 425 46" preserveAspectRatio="none"><path d="M0 46C20 46 25 0 80 0H345C400 0 405 46 425 46Z" fill="#3079a9"/></svg>
  <h2 class="why-title">Why it Works</h2>
  <h3 class="why-sub">SELLING A CAR?</h3>
  <div class="benefit" style="left:86px">
    <svg width="64" height="64" viewBox="0 0 64 64"><use href="#car" x="2" y="26" width="60" height="34"/><text x="32" y="24" text-anchor="middle" font-size="28" fill="#fff" font-family="Nunito Sans,sans-serif">$</text></svg>
    <h4>1. Valuation</h4><p>Get an instant valuation online.</p>
  </div>
  <div class="benefit" style="left:282px">
    <svg width="64" height="64" viewBox="0 0 64 64"><use href="#car" x="2" y="26" width="60" height="34"/><circle cx="42" cy="14" r="11" fill="none" stroke="#fff" stroke-width="2.5"/><path d="M36 14l5 5 9-10" fill="none" stroke="#fff" stroke-width="2.5"/></svg>
    <h4>2. Certified</h4><p>We'll inspect your car, certify it for sale and give you the best price upfront.</p>
  </div>
  <div class="benefit" style="left:454px">
    <svg width="64" height="64" viewBox="0 0 64 64"><use href="#car" x="2" y="26" width="60" height="34"/><rect x="30" y="6" width="30" height="14" rx="2" fill="none" stroke="#fff" stroke-width="2" transform="rotate(-20 45 13)"/></svg>
    <h4>3. Sold</h4><p>We'll buy your car straight away!</p>
  </div>
  <div class="btn-outline">GET OFFERS</div>
  <div class="video" role="img" aria-label="Video still: couple receiving car keys from a salesman">
    <svg class="play" width="50" height="50" viewBox="0 0 50 50"><circle cx="25" cy="25" r="24" fill="#fff" opacity=".9"/><path d="M20 15l15 10-15 10z" fill="#2f78a8"/></svg>
  </div>
</section>

<section class="deals">
  <h2 class="deals-title">Live Deals- Our Average clients saved<br>Nearly 14% off list Price</h2>
  <div class="deal" style="left:100px">
    <div class="price"><b>$89</b><span>/week</span></div>
    <div class="deal-car" role="img" aria-label="Grey sports coupe" style="background:linear-gradient(180deg,#b8bcc0,#5e6267)"></div>
    <h5>Velaro ST</h5><p>interdum vel blandit sed nulla<br>In ullamcorper est eget</p>
  </div>
  <div class="deal" style="left:360px">
    <div class="price"><b>$89</b><span>/week</span></div>
    <div class="deal-car" role="img" aria-label="White compact hatchback" style="background:linear-gradient(180deg,#f4f4f4,#c9c9c9)"></div>
    <h5>Car Brand Name</h5><p>interdum vel blandit sed nulla<br>In ullamcorper est eget</p>
  </div>
  <div class="deal" style="left:620px">
    <div class="price"><b>$89</b><span>/week</span></div>
    <div class="deal-car" role="img" aria-label="White sedan" style="background:linear-gradient(180deg,#f6f6f6,#cdcdcd)"></div>
    <h5>Car Brand Name</h5><p>interdum vel blandit sed nulla<br>In ullamcorper est eget</p>
  </div>
  <div class="deal" style="left:880px">
    <div class="price"><b>$89</b><span>/week</span></div>
    <div class="deal-car" role="img" aria-label="Silver electric sedan" style="background:linear-gradient(180deg,#e2e3e5,#8d9096)"></div>
    <h5>Car Brand Name</h5><p>interdum vel blandit sed nulla<br>In ullamcorper est eget</p>
  </div>
</section>

<footer class="site-footer">
  <nav class="footer-links"><span>How it works</span>|<span>Pricing</span>|<span>FAQ</span>|<span>Privacy Policy</span>|<span>Terms and Conditions</span>|<span>Car Reviews</span>|<span>Become a Supplier</span></nav>
  <p class="legal">Quorvex Ventures Pty Ltd T/A Quorvex ABN 00 000 000 000</p>
  <div class="social"><span></span><span></span><span></span><span></span></div>
  <div class="footer-brand">Quorvex</div>
</footer>
</body>
</html>
```